Professional Home Buyer business card needed

I need a pretty straight forward business card designed. We help people that NEED to sell their homes solve problems. We perform all types of Real Estate transactions including flip, wholesale, investment, rental property and multi family. The card will mainly be used to give to prospective Sellers but will also be given to Real Estate Investors as well. It should professional and very easy to read, most clients are older people.

Target Market(s)

Distressed home sellers as well as Real Estate investors

Industry/Entity Type

Real Estate

Contact Information for Business Card

should be a professional layout

Colors
ec1f27
ffffff
000000

Requirements
Must have
• Large logo on back and smaller one on front. should utilize Red, white, and black.
• I am thinking of using a soft touch coating on the card so keep that in mind.
• Contact info should be very easy to read, think older clients.
Nice to have
• I would like to see a design with rounded corners on the card
Should not have
• pictures of homes or other home graphics.

```html
<!DOCTYPE html>
<html lang="en">
<head>
<meta charset="UTF-8">
<title>Beacon Home Buyers – Business Card</title>
<link href="https://fonts.googleapis.com/css2?family=Open+Sans:wght@400;700&display=swap" rel="stylesheet">
<style>
  :root {
    --brand-red: #ec1f27;
    --ink: #000000;
    --paper: #ffffff;
    --page: #ffffff;
    --card-shadow: rgba(0, 0, 0, 0.18);
  }
  * { margin: 0; padding: 0; box-sizing: border-box; }
  html, body {
    width: 1200px;
    height: 1200px;
    overflow: hidden;
    background: var(--page);
    font-family: "Open Sans", Arial, sans-serif;
    color: var(--ink);
  }
  .canvas { position: relative; width: 1200px; height: 1200px; }
  .card {
    position: absolute;
    left: 254px;
    width: 694px;
    height: 396px;
    background: var(--paper);
    box-shadow: 0 1px 3px var(--card-shadow);
  }
  .card--front { top: 112px; }
  .card--back { top: 611px; }

  .wordmark {
    position: absolute;
    font-family: "Open Sans", Arial, sans-serif;
    font-weight: 700;
    color: var(--ink);
    white-space: nowrap;
    text-align: center;
    transform: translate(-50%, -50%);
    letter-spacing: 0.02em;
  }
  .card--front .wordmark { left: 347px; top: 200px; font-size: 40px; }
  .card--back .wordmark { left: 530px; top: 193px; font-size: 26px; }

  .contact-block { position: absolute; left: 42px; top: 96px; }
  .person-name {
    font-weight: 700;
    font-size: 32px;
    line-height: 1;
    color: var(--brand-red);
    letter-spacing: -0.01em;
  }
  .person-title {
    font-weight: 400;
    font-size: 22px;
    margin-top: 8px;
    line-height: 1;
  }
  .contact-list { list-style: none; margin-top: 40px; }
  .contact-item {
    display: flex;
    align-items: center;
    height: 26px;
    margin-bottom: 10px;
    font-size: 17px;
  }
  .contact-icon { width: 26px; height: 26px; margin-right: 20px; flex: none; }
  .contact-icon * { fill: none; stroke: var(--brand-red); stroke-width: 1.6; stroke-linejoin: round; stroke-linecap: round; }

  .divider {
    position: absolute;
    left: 341px;
    top: 83px;
    width: 2px;
    height: 231px;
    background: var(--brand-red);
  }
</style>
</head>
<body>
<div class="canvas">

  <section class="card card--front" aria-label="Card front">
    <div class="wordmark">Beacon Home Buyers</div>
  </section>

  <section class="card card--back" aria-label="Card back">
    <div class="contact-block">
      <div class="person-name">Daniel Reyes</div>
      <div class="person-title">Owner</div>
      <ul class="contact-list">
        <li class="contact-item">
          <svg class="contact-icon" viewBox="0 0 26 26" aria-hidden="true">
            <path d="M5 3 L9 3 L11 8 L8.5 10 C10 14 12 16 16 17.5 L18 15 L23 17 L23 21 C23 22 22 23 21 23 C11 22 4 15 3 5 C3 4 4 3 5 3 Z"/>
          </svg>
          <span>555 010 4821</span>
        </li>
        <li class="contact-item">
          <svg class="contact-icon" viewBox="0 0 26 26" aria-hidden="true">
            <rect x="2" y="5" width="22" height="16"/>
            <path d="M2 5 L13 14 L24 5 M2 21 L10 12 M24 21 L16 12"/>
          </svg>
          <span>daniel.reyes@beaconhb.com</span>
        </li>
        <li class="contact-item">
          <svg class="contact-icon" viewBox="0 0 26 26" aria-hidden="true">
            <circle cx="13" cy="13" r="11"/>
            <path d="M2 13 H24 M13 2 V24 M5.5 5 C10 9 16 17 20.5 21 M20.5 5 C16 9 10 17 5.5 21"/>
          </svg>
          <span>www.beaconhb.com</span>
        </li>
      </ul>
    </div>
    <div class="divider"></div>
    <div class="wordmark">Beacon Home Buyers</div>
  </section>

</div>
</body>
</html>
```